Corlanta yard sign to enhance advertising taking advantage of technology

Yard sign
I have uploaded my Logo and a picture of a home I built
Company Name : CORLANTA
The sign Is 27" x 18"
I want the sign to reflect that perfect day-spring/summer the one that makes you feel good- I want the customer to feel good looking at the sign so it can stay in his yard for a period of time and I want a potential customer to drive by see the sign and think I want my house to look like that. or at least start thinking I should call that company. "that is a real nice sign"

-statement: "Providing the best service to your home so you can live comfortably"
-The house picture I uploaded is optional. I jjust want something that reflects a nice day. Might have to much going on
-Logo with name to the right
-Phone1234567890
-www.Corlanta-example.net
-improve quality, improve value, increase longevity, save thousands (not sure of the best way to word quality, value, longevity and save thousands) if there is a way to sum this up even better. this is optional as well
- everything has to be clear and readable

Potential customers may take pictures of the sign. Is there a way to integrate something to enhance what happens Or at least encourage a potential customer to take pictures and share. Some kind of reaction (may not be possible) if possible let me know
Basically if there is way the yard sign can get more noticed and shared further enhancing its advertising ability. I want to try and take advantage of technology

Target Market(s)

Home owners

Industry/Entity Type

Advertising

Requirements
Must have
• logo & company name CORLANTA
• Providing the best service to your home so you can live comfortably
Nice to have
• i have uploaded an image of a home I built, I like the idea of it being used but if it does not work for what you have imagined don't use it.
• Your ideas.... I know this may seem generic but you guys have amazing talent

```html
<!DOCTYPE html>
<html lang="en">
<head>
<meta charset="UTF-8">
<title>Corlanta Yard Sign</title>
<link href="https://fonts.googleapis.com/css2?family=Montserrat:wght@500;600;700&display=swap" rel="stylesheet">
<style>
  :root {
    --orange: #ef7f1a;
    --orange-deep: #d9601a;
    --orange-light: #f7a12a;
    --green: #4f9a34;
    --green-dark: #2f7a2a;
    --green-light: #6cb33f;
    --white: #ffffff;
    --canopy: #3f6a32;
    --canopy-light: #6d8f4a;
    --stucco: #d6c7a3;
    --paver: #bdb6a8;
    --lawn: #5f8a3a;
  }
  * { margin: 0; padding: 0; box-sizing: border-box; }
  html, body { width: 1200px; height: 800px; overflow: hidden; background: var(--white); }
  body { font-family: "Montserrat", Arial, sans-serif; }
  .sign { position: relative; width: 1200px; height: 800px; background: var(--white); overflow: hidden; }

  .brand-bar { position: absolute; top: 0; left: 0; width: 1200px; height: 185px; background: var(--white); }
  .brand-name {
    position: absolute; left: 640px; top: 72px;
    font-size: 58px; font-weight: 600; letter-spacing: 2px;
    color: var(--orange); line-height: 1; white-space: nowrap;
  }
  .brand-mark {
    position: absolute; left: 1022px; top: 36px;
    width: 120px; height: 120px; border-radius: 50%;
    background: var(--orange);
  }

  .home-photo {
    position: absolute; top: 185px; left: 0; width: 1200px; height: 468px;
    background:
      linear-gradient(180deg, var(--canopy-light) 0%, var(--canopy) 22%, var(--canopy) 32%, var(--stucco) 52%, var(--stucco) 64%, var(--paver) 80%, var(--lawn) 100%);
  }

  .slogan-badge {
    position: absolute; left: 75px; top: 48px;
    width: 442px; height: 442px; border-radius: 50%;
    background: radial-gradient(circle at 45% 40%, var(--green-light) 0%, var(--green) 55%, var(--green-dark) 100%);
    border: 8px solid var(--orange);
    display: flex; flex-direction: column; align-items: center; justify-content: center;
    padding-bottom: 40px;
    color: var(--white); text-align: center; text-transform: uppercase;
    font-weight: 600; line-height: 1.08; white-space: nowrap;
  }
  .slogan-badge .lead { font-size: 44px; }
  .slogan-badge .sub { font-size: 27px; margin: 6px 0; }
  .slogan-badge .key { font-size: 50px; }
  .slogan-badge .tail { font-size: 40px; }

  .contact-bar {
    position: absolute; left: 0; top: 657px; width: 1200px; height: 143px;
    background: linear-gradient(90deg, var(--orange-deep) 0%, var(--orange-light) 50%, var(--orange-deep) 100%);
    color: var(--white);
  }
  .phone-icon { position: absolute; left: 34px; top: 26px; width: 92px; height: 92px; }
  .phone-number {
    position: absolute; left: 136px; top: 24px;
    font-size: 88px; font-weight: 600; letter-spacing: 3px; line-height: 1.1; white-space: nowrap;
  }
  .divider { position: absolute; left: 785px; top: 38px; width: 2px; height: 66px; background: var(--white); }
  .web-icon { position: absolute; left: 802px; top: 62px; width: 20px; height: 26px; }
  .web-address {
    position: absolute; left: 830px; top: 54px;
    font-size: 24px; font-weight: 600; line-height: 1.3; white-space: nowrap;
  }
</style>
</head>
<body>
<div class="sign">
  <header class="brand-bar">
    <div class="brand-name">CORLANTA</div>
    <div class="brand-mark"></div>
  </header>

  <div class="home-photo" role="img" aria-label="Photo of a custom-built stucco home with tile roof, arched windows, paver driveway, palms and landscaped lawn on a sunny day"></div>

  <div class="slogan-badge">
    <span class="lead">Providing</span>
    <span class="sub">the best service to</span>
    <span class="key">Your Home</span>
    <span class="sub">so you can live</span>
    <span class="tail">Comfortably</span>
  </div>

  <footer class="contact-bar">
    <svg class="phone-icon" viewBox="0 0 92 92" aria-hidden="true">
      <circle cx="46" cy="46" r="42" fill="none" stroke="#fff" stroke-width="5"/>
      <path d="M33 24c3-2 6-1 7 2l4 9c1 2 0 4-2 5l-3 2c2 6 7 11 13 14l2-3c1-2 3-3 5-2l9 4c3 1 4 4 2 7l-3 4c-3 3-8 4-13 2-13-6-22-15-27-28-2-5-1-10 3-13z" fill="#fff"/>
    </svg>
    <div class="phone-number">5550 142 378</div>
    <div class="divider"></div>
    <svg class="web-icon" viewBox="0 0 22 28" aria-hidden="true">
      <path d="M7 8c0-2 3-2 3 0v7l1-1c1-1 3 0 3 1l1 0c1-1 3 0 3 1h0c1-1 3 0 3 1v6c0 3-2 5-5 5h-3c-2 0-3-1-4-2l-5-6c-1-1 0-3 2-2l1 1z" fill="#fff"/>
      <path d="M8 1v3M3 4l2 2M13 4l-2 2" stroke="#fff" stroke-width="1.5"/>
    </svg>
    <div class="web-address">www.Corlanta-example.net</div>
  </footer>
</div>
</body>
</html>
```